Velgrijder

2 homepage design for my tire webshop. One for the winter and one for the summer.
2 items have to come back.
1 a filterbox option to choose tire width, height and inch
2 an option where i can sell my tire mounting service
The customer can buy tires from me but also have the option to use only my skills for mounting their own tire.
My sellingpoint is my mobile service, a webshop with his own mechanic, and my good reputation.

```html
<!DOCTYPE html>
<html lang="en">
<head>
<meta charset="utf-8">
<title>Velgrijder – Winter and Summer Homepage</title>
<link href="https://fonts.googleapis.com/css2?family=Roboto:ital,wght@0,400;0,500;0,700;0,900;1,400&display=swap" rel="stylesheet">
<style>
:root{
  --orange:#ff5a0a;
  --ink:#1f1f1f;
  --nav:#1c1c1c;
  --soft:#f4f4f4;
  --line:#e0e0e0;
  --stage:#d5d5d5;
  --muted:#8a8a8a;
  --white:#ffffff;
}
*{box-sizing:border-box;margin:0;padding:0}
html,body{width:1200px;height:2524px;overflow:hidden}
body{background:var(--stage);font-family:'Roboto',sans-serif;color:var(--ink);position:relative}
.season-label{position:absolute;top:36px;width:505px;text-align:center;font:700 21px 'Roboto',sans-serif;color:var(--white);letter-spacing:1px}
.page{position:absolute;top:94px;width:505px;background:var(--white);display:flex;flex-direction:column;overflow:hidden}
.page--winter{left:68px}
.page--summer{left:625px}
.section{position:relative;flex:none}
.inner{padding:0 46px}

/* nav */
.nav{height:53px;background:var(--nav);display:flex;align-items:center;justify-content:space-between;padding:0 46px}
.brand{font:700 11px 'Roboto',sans-serif;color:var(--white);letter-spacing:.4px}
.nav-links{display:flex;align-items:center;gap:10px;font:500 5.5px 'Roboto',sans-serif;color:var(--white);letter-spacing:.2px}
.nav-links .active{color:var(--orange)}
.lang{display:flex;align-items:center;gap:3px}
.lang-dot{width:15px;height:15px;border-radius:50%;background:#b8c4d8}

/* hero */
.hero{height:310px;overflow:hidden}
.photo{position:absolute;inset:0}
.hero-title{font:700 20px/1.25 'Roboto',sans-serif;color:var(--white);text-transform:uppercase;letter-spacing:.3px}
.pill{display:inline-flex;align-items:center;justify-content:center;border-radius:20px;font:700 5px 'Roboto',sans-serif;letter-spacing:.3px;text-transform:uppercase}
.pill--orange{background:var(--orange);color:var(--white)}
.pill--dark{background:var(--nav);color:var(--white)}
.pill--outline{border:1.2px solid var(--orange);color:var(--ink);background:transparent;height:18px;width:66px}
.chev{position:absolute;width:14px;height:26px}

/* filter */
.filter-bar{height:43px;background:var(--orange);display:flex;align-items:center;padding:0 17px;gap:6px}
.tab{position:absolute;left:17px;top:-10px;background:var(--nav);color:var(--white);font:700 9px 'Roboto',sans-serif;padding:4px 13px 5px;letter-spacing:.3px}
.tab::after{content:"";position:absolute;right:-8px;top:0;border-left:8px solid var(--nav);border-bottom:19px solid transparent}
.offer{color:var(--white);width:88px;font:400 5.5px/1.4 'Roboto',sans-serif;margin-top:9px}
.offer b{display:block;font:700 7.5px 'Roboto',sans-serif}
.select{height:16px;width:73px;background:var(--white);border-radius:10px;display:flex;align-items:center;justify-content:space-between;padding:0 8px;font:400 4.8px 'Roboto',sans-serif;color:var(--muted)}
.select::after{content:"";width:3px;height:3px;border-right:1px solid #999;border-bottom:1px solid #999;transform:rotate(45deg);margin-top:-2px}
.search-btn{height:16px;width:73px}

/* install */
.install{height:42px;background:var(--nav);display:flex;align-items:center;justify-content:flex-end;padding-right:46px;gap:10px}
.install-photo{position:absolute;left:0;top:0;bottom:0;width:265px;clip-path:polygon(0 0,100% 0,88% 100%,0 100%)}
.install-tag{position:absolute;left:34px;top:12px;background:var(--nav);color:var(--white);font:700 10px 'Roboto',sans-serif;padding:3px 9px;letter-spacing:.3px}
.install-price{position:relative;color:var(--white);font:400 5px/1.5 'Roboto',sans-serif}
.install-price b{display:block;font:700 8px 'Roboto',sans-serif}
.appoint{height:16px;width:90px;position:relative}

/* categories */
.cats{height:164px;display:flex;align-items:center;gap:6px;padding:0 46px}
.cat{position:relative;flex:1;height:98px;overflow:hidden}
.cat-label{position:absolute;left:0;top:13px;background:var(--orange);color:var(--white);font:700 9px 'Roboto',sans-serif;padding:4px 14px 4px 6px;border-radius:0 12px 12px 0;letter-spacing:.3px}
.cat-text{position:absolute;left:12px;right:12px;bottom:10px;color:var(--white);font:400 5.2px/1.5 'Roboto',sans-serif}

/* titles */
.title{font:700 15px 'Roboto',sans-serif;letter-spacing:.4px;text-transform:uppercase;color:var(--ink)}
.center{text-align:center}

/* products */
.products{height:206px;padding-top:24px}
.row-head{display:flex;justify-content:space-between;align-items:center;padding:0 46px}
.mini-filter{display:flex;align-items:center;gap:3px;font:400 5px 'Roboto',sans-serif;color:var(--muted)}
.mini-filter .select{width:30px;height:10px;border-radius:2px;border:1px solid var(--line);padding:0 4px;font-size:4.3px}
.mini-filter .select::after{width:2px;height:2px}
.cards{display:flex;gap:5px;padding:0 46px;margin-top:15px;position:relative}
.card{flex:1;height:121px;border:1px solid var(--line);text-align:center;padding-top:8px}
.tire{width:68px;height:68px;margin:0 auto;border-radius:50%;background:radial-gradient(circle,#c9ccd0 0 22%,#4a4a4a 24% 36%,#222 40% 100%)}
.card-name{font:400 6.5px 'Roboto',sans-serif;color:#444;margin-top:9px}
.card-price{font:700 10px 'Roboto',sans-serif;color:var(--orange);margin-top:4px}

/* services */
.services{height:302px;background:var(--soft);padding-top:42px}
.stripe{position:absolute;top:0;height:6px;background:var(--orange)}
.two-col{display:flex;gap:16px;padding:0 46px}
.col{flex:1;text-align:center}
.service-head{background:var(--orange);color:var(--white);font:700 6.5px 'Roboto',sans-serif;height:27px;display:flex;align-items:center;justify-content:center;letter-spacing:.3px}
.service-photo{height:104px;border:2px solid var(--orange);border-top:none}
.blurb{font:400 5.2px/1.75 'Roboto',sans-serif;color:#777;margin:8px 6px 9px}

/* special */
.special{height:159px;padding-top:38px}
.feat-row{display:flex;padding:0 46px;margin-top:18px}
.feat{flex:1;text-align:center;font:500 5.8px/1.35 'Roboto',sans-serif;text-transform:uppercase;color:var(--ink);border-left:1px solid var(--line);height:48px}
.feat:first-child{border-left:none}
.feat svg{display:block;margin:0 auto 8px;width:25px;height:27px}

/* arrivals */
.arrivals{height:220px;padding-top:20px}

/* blog */
.blog{height:314px;background:var(--soft);padding-top:48px}
.post-title{font:700 7px 'Roboto',sans-serif;text-transform:uppercase;letter-spacing:.2px;margin-top:20px}
.post-date{font:500 5px 'Roboto',sans-serif;color:var(--orange);margin:4px 0 9px;display:flex;align-items:center;justify-content:center;gap:3px}
.post-photo{height:107px}

/* how */
.how{height:167px;background:var(--orange);padding-top:36px;text-align:center}
.how .title{color:var(--white)}
.steps{display:flex;justify-content:space-between;padding:0 70px;margin-top:14px;position:relative}
.step{width:60px;text-align:center;color:var(--white);font:700 6px 'Roboto',sans-serif;text-transform:uppercase;white-space:nowrap}
.step-circle{width:60px;height:60px;border-radius:50%;background:var(--white);display:flex;align-items:center;justify-content:center;margin-bottom:9px}
.step-circle svg{width:32px;height:32px}
.step-arrow{position:absolute;top:20px;width:34px;height:14px}

/* reviews */
.reviews{height:211px;padding-top:42px}
.review{flex:1;border:1px solid var(--line);padding:13px 12px;text-align:left;height:100px;margin-top:18px;position:relative}
.review-head{display:flex;gap:8px;align-items:flex-start}
.avatar{width:27px;height:27px;border-radius:50%;background:linear-gradient(160deg,#c9a58b,#5b4c44)}
.reviewer{font:700 8px 'Roboto',sans-serif}
.reviewer small{display:block;font:400 4.8px 'Roboto',sans-serif;color:var(--muted);margin-top:2px}
.stars{display:flex;gap:1px;margin-top:3px}
.badge{position:absolute;right:12px;top:13px;width:36px;height:12px;border-radius:3px;background:#e6e9ef}
.quote{font:italic 400 5.2px/1.75 'Roboto',sans-serif;color:#888;margin-top:10px}

/* footer */
.footer{height:167px;background:var(--nav);color:var(--white);display:flex;gap:18px;padding:34px 46px 0}
.f-col{font:400 5.2px/1.7 'Roboto',sans-serif}
.f-head{font:500 8px 'Roboto',sans-serif;margin-bottom:6px;display:flex;align-items:center;gap:4px;text-transform:uppercase}
.f-link{color:var(--orange)}
.socials{display:flex;gap:3px;margin-bottom:12px}
.socials span{width:14px;height:14px;border-radius:50%;border:1px solid var(--white)}
</style>
</head>
<body>

<svg width="0" height="0" style="position:absolute">
  <defs>
    <symbol id="chev-left" viewBox="0 0 14 26"><polyline points="12,1 2,13 12,25" fill="none" stroke="currentColor" stroke-width="1.5"/></symbol>
    <symbol id="chev-right" viewBox="0 0 14 26"><polyline points="2,1 12,13 2,25" fill="none" stroke="currentColor" stroke-width="1.5"/></symbol>
    <symbol id="star" viewBox="0 0 10 10"><polygon points="5,0.5 6.3,3.6 9.6,3.8 7,6 7.9,9.3 5,7.5 2.1,9.3 3,6 0.4,3.8 3.7,3.6" fill="#ff5a0a"/></symbol>
    <symbol id="cal" viewBox="0 0 10 10"><rect x="1" y="2" width="8" height="7" fill="none" stroke="#ff5a0a"/><line x1="1" y1="4" x2="9" y2="4" stroke="#ff5a0a"/><line x1="3" y1="1" x2="3" y2="3" stroke="#ff5a0a"/><line x1="7" y1="1" x2="7" y2="3" stroke="#ff5a0a"/></symbol>
    <symbol id="i-cheap" viewBox="0 0 26 28"><g fill="none" stroke="#ff5a0a" stroke-width="1.3"><rect x="3" y="3" width="14" height="18" rx="1"/><line x1="6" y1="8" x2="14" y2="8"/><line x1="6" y1="12" x2="12" y2="12"/><circle cx="17" cy="18" r="6"/><path d="M15 18h4M17 16v4"/></g></symbol>
    <symbol id="i-cone" viewBox="0 0 26 28"><g fill="none" stroke="#ff5a0a" stroke-width="1.3"><path d="M10 3h6l5 20H5z"/><line x1="8" y1="11" x2="18" y2="11"/><line x1="7" y1="17" x2="19" y2="17"/><line x1="2" y1="25" x2="24" y2="25"/></g></symbol>
    <symbol id="i-happy" viewBox="0 0 26 28"><g fill="none" stroke="#ff5a0a" stroke-width="1.3"><circle cx="9" cy="10" r="5"/><circle cx="18" cy="10" r="5"/><path d="M3 24c1-5 11-5 12 0M12 24c1-5 11-5 12 0"/><polygon points="13,1 14,3.5 16.5,3.5 14.5,5 15.3,7.5 13,6 10.7,7.5 11.5,5 9.5,3.5 12,3.5"/></g></symbol>
    <symbol id="i-cal7" viewBox="0 0 26 28"><g fill="none" stroke="#ff5a0a" stroke-width="1.3"><rect x="2" y="4" width="19" height="18" rx="1"/><line x1="2" y1="9" x2="21" y2="9"/><line x1="7" y1="2" x2="7" y2="6"/><line x1="16" y1="2" x2="16" y2="6"/><rect x="5" y="12" width="3" height="3"/><rect x="10" y="12" width="3" height="3"/><rect x="5" y="17" width="3" height="3"/><circle cx="20" cy="21" r="5" fill="#fff"/><path d="M20 18v3h2"/></g></symbol>
    <symbol id="i-cart" viewBox="0 0 32 32"><g fill="none" stroke="#ff5a0a" stroke-width="1.5"><path d="M3 6h4l4 15h14l3-10H9"/><circle cx="13" cy="26" r="2"/><circle cx="23" cy="26" r="2"/><path d="M14 14h10"/></g></symbol>
    <symbol id="i-book" viewBox="0 0 32 32"><g fill="none" stroke="#ff5a0a" stroke-width="1.5"><rect x="4" y="6" width="24" height="22" rx="2"/><line x1="4" y1="12" x2="28" y2="12"/><line x1="10" y1="3" x2="10" y2="8"/><line x1="22" y1="3" x2="22" y2="8"/><circle cx="10" cy="17" r="1.5"/><circle cx="16" cy="17" r="1.5"/><circle cx="22" cy="17" r="1.5"/><circle cx="10" cy="23" r="1.5"/><circle cx="16" cy="23" r="1.5"/></g></symbol>
    <symbol id="i-home" viewBox="0 0 32 32"><g fill="none" stroke="#ff5a0a" stroke-width="1.5"><path d="M3 26l9-13 5 6 4-5 8 12z"/><line x1="2" y1="28" x2="30" y2="28"/><path d="M20 7l3-3 3 3M23 4v8"/></g></symbol>
    <symbol id="i-pay" viewBox="0 0 32 32"><g fill="none" stroke="#ff5a0a" stroke-width="1.5"><rect x="8" y="4" width="18" height="11" rx="1"/><circle cx="17" cy="9.5" r="2.5"/><path d="M3 20h8l5 2h7c2 0 2 3 0 3h-7M3 28h14l11-5"/></g></symbol>
    <symbol id="arrow-curve" viewBox="0 0 34 14"><path d="M2 10C10 0 22 0 30 10" fill="none" stroke="#fff" stroke-width="1" stroke-dasharray="2 2"/><polyline points="26,9 30,11 31,7" fill="none" stroke="#fff" stroke-width="1"/></symbol>
    <symbol id="i-pin" viewBox="0 0 10 10"><path d="M5 9.5S1.5 6 1.5 4a3.5 3.5 0 0 1 7 0c0 2-3.5 5.5-3.5 5.5z" fill="none" stroke="#fff"/><circle cx="5" cy="4" r="1.2" fill="none" stroke="#fff"/></symbol>
    <symbol id="i-mail" viewBox="0 0 10 10"><rect x="0.8" y="2" width="8.4" height="6" fill="none" stroke="#fff"/><polyline points="1,2.3 5,5.5 9,2.3" fill="none" stroke="#fff"/></symbol>
    <symbol id="i-phone" viewBox="0 0 10 10"><path d="M2 1l2 2-1 1.5c.6 1.3 1.3 2 2.5 2.5L7 6l2 2-1.2 1.2C5 9 1 5 .8 2.2z" fill="none" stroke="#fff"/></symbol>
    <symbol id="i-search" viewBox="0 0 10 10"><circle cx="4" cy="4" r="3" fill="none" stroke="#fff" stroke-width="1.2"/><line x1="6.3" y1="6.3" x2="9" y2="9" stroke="#fff" stroke-width="1.2"/></symbol>
  </defs>
</svg>

<div class="season-label" style="left:68px">WINTER</div>
<div class="season-label" style="left:625px">SUMMER</div>

<!-- ================= WINTER ================= -->
<main class="page page--winter">
  <header class="section nav">
    <div class="brand">VELGRIJDER</div>
    <nav class="nav-links">
      <span class="active">HOME</span><span>ABOUT US</span><span>SERVICES</span><span>BLOG</span><span>SHOP</span><span>CONTACT US</span>
      <span class="lang"><span class="lang-dot"></span>ENG ˅</span>
      <svg width="7" height="7"><use href="#i-search"/></svg>
    </nav>
  </header>

  <section class="section hero">
    <div class="photo" role="img" aria-label="Snowy mountain landscape with a stack of winter tires in the snow" style="background:linear-gradient(180deg,#6d7785 0%,#b9c1cb 35%,#e9edf1 62%,#ffffff 100%)"></div>
    <div style="position:absolute;left:0;right:0;top:52px;text-align:center">
      <div class="hero-title">Velgrijder<br>for all vehicle type tire</div>
      <span class="pill pill--orange" style="width:80px;height:17px;margin-top:6px">Check work area</span>
    </div>
    <svg class="chev" style="left:16px;top:118px;color:#fff"><use href="#chev-left"/></svg>
    <svg class="chev" style="right:16px;top:118px;color:#fff"><use href="#chev-right"/></svg>
  </section>

  <section class="section filter-bar">
    <div class="tab">NEW TIRE</div>
    <div class="offer">New Tires + Mounting<b>FROM $41 P/B</b></div>
    <div class="select">Width</div><div class="select">Height</div><div class="select">Diameter</div><div class="select">Season</div>
    <span class="pill pill--dark search-btn">Search</span>
  </section>

  <section class="section install">
    <div class="install-photo" role="img" aria-label="Car wheel driving through snow" style="background:linear-gradient(90deg,#cfd6de,#5e646c)"></div>
    <div class="install-tag">INSTALLATION ONLY</div>
    <div class="install-price">Installation Only On Location<b>FROM $16.25 P/B</b></div>
    <span class="pill pill--orange appoint">Make an appointment</span>
  </section>

  <section class="section cats">
    <div class="cat"><div class="photo" role="img" aria-label="Winter tires in snow" style="background:linear-gradient(160deg,#c9d3dc,#3a3f45)"></div><div class="cat-label">WINTER TIRE</div><div class="cat-text">Sturdy tread for every road, fitted at your door</div></div>
    <div class="cat"><div class="photo" role="img" aria-label="All season tire close-up" style="background:linear-gradient(160deg,#aab4be,#2f3338)"></div><div class="cat-label">ALL SESAON TIRE</div><div class="cat-text">Sturdy tread for every road, fitted at your door</div></div>
    <div class="cat"><div class="photo" role="img" aria-label="Car wheel on a snowy road" style="background:linear-gradient(160deg,#dfe5ea,#4a5058)"></div><div class="cat-label">WINTER TIRE</div><div class="cat-text">Sturdy tread for every road, fitted at your door</div></div>
  </section>

  <section class="section products">
    <h2 class="title center">Our latest products</h2>
    <div class="cards">
      <div class="card"><div class="tire" role="img" aria-label="Tire with alloy rim"></div><div class="card-name">Lorem ipsum dolor sit</div><div class="card-price">$35.00</div></div>
      <div class="card"><div class="tire" role="img" aria-label="Tire with alloy rim"></div><div class="card-name">Lorem ipsum dolor sit</div><div class="card-price">$35.00</div></div>
      <div class="card"><div class="tire" role="img" aria-label="Tire with alloy rim"></div><div class="card-name">Lorem ipsum dolor sit</div><div class="card-price">$35.00</div></div>
      <div class="card"><div class="tire" role="img" aria-label="Off-road tire" style="background:radial-gradient(circle,#333 0 30%,#1c1c1c 34% 100%)"></div><div class="card-name">Lorem ipsum dolor sit</div><div class="card-price">$35.00</div></div>
    </div>
    <svg class="chev" style="left:16px;top:96px;color:#444"><use href="#chev-left"/></svg>
    <svg class="chev" style="right:16px;top:96px;color:#444"><use href="#chev-right"/></svg>
  </section>

  <section class="section services">
    <div class="stripe" style="left:142px;right:0;clip-path:polygon(2% 0,100% 0,100% 100%,0 100%)"></div>
    <h2 class="title center" style="margin-bottom:10px">Our services</h2>
    <div class="two-col">
      <div class="col"><div class="service-head">BUY TIRES</div><div class="service-photo" role="img" aria-label="Tire with snow chains on a snowy road" style="background:linear-gradient(100deg,#5d6f86,#c6d3df 60%,#eef3f7)"></div><p class="blurb">Pick the right tires in our webshop and our own mechanic fits them at your home, your work or wherever your car is parked today.</p><span class="pill pill--outline">Learn more</span></div>
      <div class="col"><div class="service-head">MOUNTING SERVICE</div><div class="service-photo" role="img" aria-label="Close-up of a mounted tire on a car" style="background:linear-gradient(100deg,#2b2b2b,#6b6b6b 55%,#d9d9d9)"></div><p class="blurb">Already own a set? Book only our mounting service and we bring the tools, balance the wheels and check the pressure on the spot.</p><span class="pill pill--outline">Learn more</span></div>
    </div>
  </section>

  <section class="section special">
    <div class="stripe" style="left:0;width:362px;clip-path:polygon(0 0,100% 0,98% 100%,0 100%)"></div>
    <h2 class="title center">What my company so special</h2>
    <div class="feat-row">
      <div class="feat"><svg><use href="#i-cheap"/></svg>Cheap</div>
      <div class="feat"><svg><use href="#i-cone"/></svg>We arrange from a to z</div>
      <div class="feat"><svg><use href="#i-happy"/></svg>Satisfied customer<br>9.5 scores</div>
      <div class="feat"><svg><use href="#i-cal7"/></svg>Opens 7 days</div>
    </div>
  </section>

  <section class="section arrivals">
    <div class="row-head">
      <h2 class="title">New arrivals</h2>
      <div class="mini-filter">Filter <span class="select">Width</span><span class="select">Height</span><span class="select">Inch</span></div>
    </div>
    <div class="cards">
      <div class="card"><div class="tire" role="img" aria-label="Tire with silver rim"></div><div class="card-name">Lorem ipsum dolor sit</div><div class="card-price">$35.00</div></div>
      <div class="card"><div class="tire" role="img" aria-label="Tire with silver rim"></div><div class="card-name">Lorem ipsum dolor sit</div><div class="card-price">$35.00</div></div>
      <div class="card"><div class="tire" role="img" aria-label="Pair of tires with rims"></div><div class="card-name">Lorem ipsum dolor sit</div><div class="card-price">$35.00</div></div>
      <div class="card"><div class="tire" role="img" aria-label="Tire with white rim"></div><div class="card-name">Lorem ipsum dolor sit</div><div class="card-price">$35.00</div></div>
    </div>
    <svg class="chev" style="left:16px;top:95px;color:#444"><use href="#chev-left"/></svg>
    <svg class="chev" style="right:16px;top:95px;color:#444"><use href="#chev-right"/></svg>
  </section>

  <section class="section blog">
    <h2 class="title center">Latest blog</h2>
    <div class="two-col">
      <div class="col"><div class="post-title">Lorem ipsum dolor sit</div><div class="post-date"><svg width="6" height="6"><use href="#cal"/></svg>AUG 05, 2018</div><div class="post-photo" role="img" aria-label="Mechanic changing a tire in a workshop" style="background:linear-gradient(120deg,#2f2f2f,#8a7d70 55%,#cfcac4)"></div><p class="blurb">When the temperature drops below seven degrees, winter tires grip better. Here is how to know it is time to switch your set.</p><span class="pill pill--outline">Learn more</span></div>
      <div class="col"><div class="post-title">Lorem ipsum dolor sit</div><div class="post-date"><svg width="6" height="6"><use href="#cal"/></svg>AUG 05, 2018</div><div class="post-photo" role="img" aria-label="Winter tire in front of snowy pine trees" style="background:linear-gradient(180deg,#9fb2c4,#e9eef2 60%,#7b8086)"></div><p class="blurb">Storing your off-season tires the right way keeps them in shape longer. A few simple steps save you money every single year.</p><span class="pill pill--outline">Learn more</span></div>
    </div>
  </section>

  <section class="section how">
    <h2 class="title">How things work</h2>
    <div class="steps">
      <div class="step"><div class="step-circle"><svg><use href="#i-cart"/></svg></div>Buy online</div>
      <div class="step"><div class="step-circle"><svg><use href="#i-book"/></svg></div>Make an appointment</div>
      <div class="step"><div class="step-circle"><svg><use href="#i-home"/></svg></div>Mounting at home</div>
      <div class="step"><div class="step-circle"><svg><use href="#i-pay"/></svg></div>Pay after</div>
      <svg class="step-arrow" style="left:133px"><use href="#arrow-curve"/></svg>
      <svg class="step-arrow" style="left:236px"><use href="#arrow-curve"/></svg>
      <svg class="step-arrow" style="left:338px"><use href="#arrow-curve"/></svg>
    </div>
  </section>

  <section class="section reviews">
    <h2 class="title center">Customer reviews</h2>
    <div class="two-col">
      <div class="review"><div class="review-head"><div class="avatar" role="img" aria-label="Customer portrait"></div><div class="reviewer">Jan Peters<small>Company name</small><div class="stars"><svg width="5" height="5"><use href="#star"/></svg><svg width="5" height="5"><use href="#star"/></svg><svg width="5" height="5"><use href="#star"/></svg><svg width="5" height="5"><use href="#star"/></svg><svg width="5" height="5"><use href="#star"/></svg></div></div></div><div class="badge"></div><p class="quote">The mechanic came to my driveway on time, swapped all four tires in under an hour and left everything clean. Friendly service at a fair price, I will book again.</p></div>
      <div class="review"><div class="review-head"><div class="avatar" role="img" aria-label="Customer portrait" style="background:linear-gradient(160deg,#d8b59a,#3f4d63)"></div><div class="reviewer">Jan Peters<small>Company name</small><div class="stars"><svg width="5" height="5"><use href="#star"/></svg><svg width="5" height="5"><use href="#star"/></svg><svg width="5" height="5"><use href="#star"/></svg><svg width="5" height="5"><use href="#star"/></svg><svg width="5" height="5"><use href="#star"/></svg></div></div></div><div class="badge"></div><p class="quote">Ordered new summer tires online and had them mounted at my office the next day. Clear prices, quick help and a mechanic who really knows his work. Recommended.</p></div>
    </div>
  </section>

  <footer class="section footer">
    <div class="f-col" style="width:118px"><div class="brand" style="margin-bottom:8px">VELGRIJDER</div>Your mobile tire service with its own mechanic. We bring new tires, mounting and balancing to your door, seven days a week, across the whole region.</div>
    <div class="f-col" style="width:100px">
      <div class="f-head"><svg width="8" height="8"><use href="#i-pin"/></svg>Location</div>12 Werkplaatsstraat, 3511 AB Utrecht, open for mobile visits
      <div class="f-head" style="margin-top:8px"><svg width="8" height="8"><use href="#i-mail"/></svg>Email</div><span class="f-link">hallo@velgrijder-mail.nl</span>
      <div class="f-head" style="margin-top:8px"><svg width="8" height="8"><use href="#i-phone"/></svg>Phone</div>+31 20 555 0147
    </div>
    <div class="f-col" style="width:60px"><div class="f-head">Links</div>HOME<br>ABOUT US<br>SERVICES<br>BLOG<br>SHOP<br>PAGES<br>CONTACT US</div>
    <div class="f-col"><div class="f-head">Follow us</div><div class="socials"><span></span><span></span><span></span><span></span></div>© 2021 All Rights reserved<br>Terms &amp; Conditions</div>
  </footer>
</main>

<!-- ================= SUMMER ================= -->
<main class="page page--summer">
  <header class="section nav">
    <div class="brand">VELGRIJDER</div>
    <nav class="nav-links">
      <span class="active">HOME</span><span>ABOUT US</span><span>SERVICES</span><span>BLOG</span><span>SHOP</span><span>CONTACT US</span>
      <span class="lang"><span class="lang-dot"></span>ENG ˅</span>
      <svg width="7" height="7"><use href="#i-search"/></svg>
    </nav>
  </header>

  <section class="section hero" style="height:263px">
    <div class="photo" role="img" aria-label="Two summer tires standing on an asphalt road with trees behind" style="background:linear-gradient(180deg,#b9c0b2 0%,#7f8a6a 35%,#4a4a44 65%,#2a2a2a 100%)"></div>
    <div style="position:absolute;left:235px;top:78px;width:210px;height:120px;background:rgba(20,20,20,.85);border-left:3px solid var(--orange);padding:10px 14px">
      <div class="hero-title" style="font-size:20px;line-height:1.2">Velgrijder<br>for all vehicle<br>type tire</div>
      <span class="pill pill--orange" style="width:80px;height:17px;margin-top:8px">Check work area</span>
    </div>
    <svg class="chev" style="left:16px;top:118px;color:#fff"><use href="#chev-left"/></svg>
    <svg class="chev" style="right:16px;top:118px;color:#fff"><use href="#chev-right"/></svg>
  </section>

  <section class="section filter-bar">
    <div class="tab">NEW TIRE</div>
    <div class="offer">New Tires + Mounting<b>FROM $41 P/B</b></div>
    <div class="select">Width</div><div class="select">Height</div><div class="select">Diameter</div><div class="select">Season</div>
    <span class="pill pill--dark search-btn">Search</span>
  </section>

  <section class="section install" style="height:43px">
    <div class="install-photo" role="img" aria-label="Mechanic fitting a wheel on a car" style="background:linear-gradient(90deg,#3c3c3c,#9a9a9a 60%,#d6d6d6)"></div>
    <div class="install-tag">INSTALLATION ONLY</div>
    <div class="install-price">Installation Only On Location<b>FROM $16.25 P/B</b></div>
    <span class="pill pill--orange appoint">Make an appointment</span>
  </section>

  <section class="section cats" style="height:159px;align-items:flex-start;padding-top:42px">
    <div class="cat"><div class="photo" role="img" aria-label="Row of summer tires" style="background:linear-gradient(160deg,#cfd3d6,#2e3135)"></div><div class="cat-label">SUMMER TIRE</div><div class="cat-text">Sturdy tread for every road, fitted at your door</div></div>
    <div class="cat"><div class="photo" role="img" aria-label="All season tires on display" style="background:linear-gradient(160deg,#8fb0cf,#2a2d31)"></div><div class="cat-label">ALL SESAON TIRE</div><div class="cat-text">Sturdy tread for every road, fitted at your door</div></div>
    <div class="cat"><div class="photo" role="img" aria-label="Car wheel on a summer road" style="background:linear-gradient(160deg,#9aa39a,#2f3236)"></div><div class="cat-label">SUMMER TIRE</div><div class="cat-text">Sturdy tread for every road, fitted at your door</div></div>
  </section>

  <section class="section products" style="height:218px;padding-top:18px">
    <div class="row-head">
      <h2 class="title">Our latest products</h2>
      <div class="mini-filter">Filter <span class="select">Width</span><span class="select">Height</span><span class="select">Inch</span></div>
    </div>
    <div class="cards">
      <div class="card"><div class="tire" role="img" aria-label="Tire with alloy rim"></div><div class="card-name">Lorem ipsum dolor sit</div><div class="card-price">$35.00</div></div>
      <div class="card"><div class="tire" role="img" aria-label="Tire with alloy rim"></div><div class="card-name">Lorem ipsum dolor sit</div><div class="card-price">$35.00</div></div>
      <div class="card"><div class="tire" role="img" aria-label="Tire with alloy rim"></div><div class="card-name">Lorem ipsum dolor sit</div><div class="card-price">$35.00</div></div>
      <div class="card"><div class="tire" role="img" aria-label="Tire with black alloy rim" style="background:radial-gradient(circle,#9aa3b0 0 20%,#2b2f36 24% 38%,#1c1c1c 42% 100%)"></div><div class="card-name">Lorem ipsum dolor sit</div><div class="card-price">$35.00</div></div>
    </div>
    <svg class="chev" style="left:16px;top:95px;color:#444"><use href="#chev-left"/></svg>
    <svg class="chev" style="right:16px;top:95px;color:#444"><use href="#chev-right"/></svg>
  </section>

  <section class="section services" style="height:299px">
    <div class="stripe" style="left:142px;right:0;clip-path:polygon(2% 0,100% 0,100% 100%,0 100%)"></div>
    <h2 class="title center" style="margin-bottom:10px">Our services</h2>
    <div class="two-col">
      <div class="col"><div class="service-head">BUY TIRES</div><div class="service-photo" role="img" aria-label="Tire splashing through water on a wet road" style="background:linear-gradient(120deg,#1e1e1e,#5a5a5a 55%,#bdbdbd)"></div><p class="blurb">Pick the right tires in our webshop and our own mechanic fits them at your home, your work or wherever your car is parked today.</p><span class="pill pill--outline">Learn more</span></div>
      <div class="col"><div class="service-head">MOUNTING SERVICE</div><div class="service-photo" role="img" aria-label="Close-up of a mounted tire on a car" style="background:linear-gradient(100deg,#2b2b2b,#6b6b6b 55%,#d9d9d9)"></div><p class="blurb">Already own a set? Book only our mounting service and we bring the tools, balance the wheels and check the pressure on the spot.</p><span class="pill pill--outline">Learn more</span></div>
    </div>
  </section>

  <section class="section special" style="height:157px">
    <div class="stripe" style="left:0;width:362px;clip-path:polygon(0 0,100% 0,98% 100%,0 100%)"></div>
    <h2 class="title center">What my company so special</h2>
    <div class="feat-row">
      <div class="feat"><svg><use href="#i-cheap"/></svg>Cheap</div>
      <div class="feat"><svg><use href="#i-cone"/></svg>We arrange from a to z</div>
      <div class="feat"><svg><use href="#i-happy"/></svg>Satisfied customer<br>9.5 scores</div>
      <div class="feat"><svg><use href="#i-cal7"/></svg>Opens 7 days</div>
    </div>
  </section>

  <section class="section arrivals" style="height:216px">
    <div class="row-head">
      <h2 class="title">New arrivals</h2>
      <div class="mini-filter">Filter <span class="select">Width</span><span class="select">Height</span><span class="select">Inch</span></div>
    </div>
    <div class="cards">
      <div class="card"><div class="tire" role="img" aria-label="Tire with silver rim"></div><div class="card-name">Lorem ipsum dolor sit</div><div class="card-price">$35.00</div></div>
      <div class="card"><div class="tire" role="img" aria-label="Tire with silver rim"></div><div class="card-name">Lorem ipsum dolor sit</div><div class="card-price">$35.00</div></div>
      <div class="card"><div class="tire" role="img" aria-label="Tire seen from the tread side" style="width:28px;border-radius:8px;background:linear-gradient(90deg,#111,#3a3a3a,#111)"></div><div class="card-name">Lorem ipsum dolor sit</div><div class="card-price">$35.00</div></div>
      <div class="card"><div class="tire" role="img" aria-label="Tire with white rim"></div><div class="card-name">Lorem ipsum dolor sit</div><div class="card-price">$35.00</div></div>
    </div>
    <svg class="chev" style="left:16px;top:95px;color:#444"><use href="#chev-left"/></svg>
    <svg class="chev" style="right:16px;top:95px;color:#444"><use href="#chev-right"/></svg>
  </section>

  <section class="section blog" style="height:318px">
    <h2 class="title center">Latest blog</h2>
    <div class="two-col">
      <div class="col"><div class="post-title">Lorem ipsum dolor sit</div><div class="post-date"><svg width="6" height="6"><use href="#cal"/></svg>AUG 05, 2018</div><div class="post-photo" role="img" aria-label="Mechanic holding a tire with rim in a workshop" style="background:linear-gradient(120deg,#5b6470,#b9bec4 55%,#e4e6e8)"></div><p class="blurb">When the temperature drops below seven degrees, winter tires grip better. Here is how to know it is time to switch your set.</p><span class="pill pill--outline">Learn more</span></div>
      <div class="col"><div class="post-title">Lorem ipsum dolor sit</div><div class="post-date"><svg width="6" height="6"><use href="#cal"/></svg>AUG 05, 2018</div><div class="post-photo" role="img" aria-label="Mechanic balancing a wheel on a machine" style="background:linear-gradient(120deg,#1f1f1f,#565656 55%,#a7a7a7)"></div><p class="blurb">Storing your off-season tires the right way keeps them in shape longer. A few simple steps save you money every single year.</p><span class="pill pill--outline">Learn more</span></div>
    </div>
  </section>

  <section class="section how">
    <h2 class="title">How things work</h2>
    <div class="steps">
      <div class="step"><div class="step-circle"><svg><use href="#i-cart"/></svg></div>Buy online</div>
      <div class="step"><div class="step-circle"><svg><use href="#i-book"/></svg></div>Make an appointment</div>
      <div class="step"><div class="step-circle"><svg><use href="#i-home"/></svg></div>Mounting at home</div>
      <div class="step"><div class="step-circle"><svg><use href="#i-pay"/></svg></div>Pay after</div>
      <svg class="step-arrow" style="left:133px"><use href="#arrow-curve"/></svg>
      <svg class="step-arrow" style="left:236px"><use href="#arrow-curve"/></svg>
      <svg class="step-arrow" style="left:338px"><use href="#arrow-curve"/></svg>
    </div>
  </section>

  <section class="section reviews">
    <h2 class="title center">Customer reviews</h2>
    <div class="two-col">
      <div class="review"><div class="review-head"><div class="avatar" role="img" aria-label="Customer portrait"></div><div class="reviewer">Jan Peters<small>Company name</small><div class="stars"><svg width="5" height="5"><use href="#star"/></svg><svg width="5" height="5"><use href="#star"/></svg><svg width="5" height="5"><use href="#star"/></svg><svg width="5" height="5"><use href="#star"/></svg><svg width="5" height="5"><use href="#star"/></svg></div></div></div><div class="badge"></div><p class="quote">The mechanic came to my driveway on time, swapped all four tires in under an hour and left everything clean. Friendly service at a fair price, I will book again.</p></div>
      <div class="review"><div class="review-head"><div class="avatar" role="img" aria-label="Customer portrait" style="background:linear-gradient(160deg,#d8b59a,#3f4d63)"></div><div class="reviewer">Jan Peters<small>Company name</small><div class="stars"><svg width="5" height="5"><use href="#star"/></svg><svg width="5" height="5"><use href="#star"/></svg><svg width="5" height="5"><use href="#star"/></svg><svg width="5" height="5"><use href="#star"/></svg><svg width="5" height="5"><use href="#star"/></svg></div></div></div><div class="badge"></div><p class="quote">Ordered new summer tires online and had them mounted at my office the next day. Clear prices, quick help and a mechanic who really knows his work. Recommended.</p></div>
    </div>
  </section>

  <footer class="section footer" style="height:164px">
    <div class="f-col" style="width:118px"><div class="brand" style="margin-bottom:8px">VELGRIJDER</div>Your mobile tire service with its own mechanic. We bring new tires, mounting and balancing to your door, seven days a week, across the whole region.</div>
    <div class="f-col" style="width:100px">
      <div class="f-head"><svg width="8" height="8"><use href="#i-pin"/></svg>Location</div>12 Werkplaatsstraat, 3511 AB Utrecht, open for mobile visits
      <div class="f-head" style="margin-top:8px"><svg width="8" height="8"><use href="#i-mail"/></svg>Email</div><span class="f-link">hallo@velgrijder-mail.nl</span>
      <div class="f-head" style="margin-top:8px"><svg width="8" height="8"><use href="#i-phone"/></svg>Phone</div>+31 20 555 0147
    </div>
    <div class="f-col" style="width:60px"><div class="f-head">Links</div>HOME<br>ABOUT US<br>SERVICES<br>BLOG<br>SHOP<br>PAGES<br>CONTACT US</div>
    <div class="f-col"><div class="f-head">Follow us</div><div class="socials"><span></span><span></span><span></span><span></span></div>© 2021 All Rights reserved<br>Terms &amp; Conditions</div>
  </footer>
</main>

</body>
</html>
```